Holiday Rental Company Flyer Design (DL not A5)

Note from PixelFolk Administration: The category sizing selected is A5, however the project requires DL sized artwork. Please refer to the DL template link below while the 'Special Requirements' are updated accordingly.

Project Brief:
We need a double sided DL flyer designed for an up market Holiday Rental Company that portrays a personalised approach to property management. These are to be used for letter box drops to homes we're specifically targeting so the design should be modern, complimentary colour palette, uncluttered & visually appealing.

Please Download the DL Template from Quillmark here: http://www.quillmark.com.au/qm/ns/propath/UploadResources.aspx?selectedTab=0?pfid=BFB&pf_id=BFB&xnav=easypath-upload-image#Templates

Target Market(s)

Wealthy Home Owners

Industry/Entity Type

It Company

Font styles to use
Other font styles liked:
• Avant Garde Extra Light & Demi

Colors
33b8a4

Requirements
Must have
• DL Flyer sizes (210mm width x 99mm width, plus 3mm bleed)
• Front: Logo, Main Image & Grab
• Back: Contact Details & Brief Description of our business
• Images: Ideally the main image should be the house with the pool but alternatively a lifestyle images could also be used.
Nice to have
• A creative designer!
Should not have
• Clutter & busy designs

```html
<!DOCTYPE html>
<html lang="en">
<head>
<meta charset="utf-8">
<title>Harbourline Stays – DL Flyer</title>
<link rel="stylesheet" href="https://fonts.googleapis.com/css2?family=Montserrat:wght@200;300;400;700&family=Crimson+Text:wght@400&display=swap">
<style>
  :root {
    --teal: #33b8a4;
    --teal-deep: #2aa893;
    --grey-strip: #c9cbcc;
    --ink: #2b2b2b;
    --white: #ffffff;
    --page: #ffffff;
  }
  * { margin: 0; padding: 0; box-sizing: border-box; }
  html, body {
    width: 1200px; height: 1153px; overflow: hidden;
    background: var(--page);
  }
  .sheet { position: relative; width: 1200px; height: 1153px; }

  .flyer {
    position: absolute; top: 63px;
    width: 474px; height: 1001px;
    background: var(--white);
    box-shadow: 0 2px 8px rgba(0,0,0,0.18);
    overflow: hidden;
  }
  .flyer--back { left: 73px; }
  .flyer--front { left: 637px; width: 469px; }
  .flyer__shapes { position: absolute; inset: 0; width: 100%; height: 100%; }

  /* Back side */
  .headline {
    position: absolute; left: 57px; top: 48px;
    color: var(--white);
    font-family: "Montserrat", sans-serif;
    font-size: 35px; line-height: 40px; letter-spacing: 1px;
    text-transform: uppercase;
  }
  .headline__light { display: block; font-weight: 300; }
  .headline__bold { display: block; font-weight: 700; letter-spacing: 2px; }

  .intro {
    position: absolute; left: 57px; top: 444px; width: 385px;
    font-family: "Crimson Text", serif;
    font-size: 14px; line-height: 17.5px; color: var(--ink);
  }
  .intro p { margin-bottom: 17px; }
  .intro__dropcap {
    float: left; color: var(--teal);
    font-size: 62px; line-height: 48px;
    margin: 2px 4px 0 0;
  }

  .contact {
    position: absolute; left: 57px; top: 702px; width: 400px;
    color: var(--white);
    font-family: "Montserrat", sans-serif; font-weight: 400;
  }
  .contact__lead { font-size: 13.5px; line-height: 20px; margin-bottom: 30px; }
  .contact__list { list-style: none; font-size: 14.5px; }
  .contact__list li { display: flex; align-items: center; height: 31px; }
  .contact__icon { width: 18px; height: 18px; margin-right: 10px; flex: none; }
  .contact__address { font-size: 14.5px; margin-top: 14px; }

  /* Front side */
  .brand {
    position: absolute; left: 185px; top: 42px; width: 270px;
    text-align: center; color: var(--white);
    font-family: "Montserrat", sans-serif; font-weight: 200;
    font-size: 25px; line-height: 36px; letter-spacing: 2px;
  }
  .brand__mark {
    display: block; width: 36px; height: 36px; margin: 14px auto 0;
    border: 1.5px solid var(--white); border-radius: 50%;
  }
  .tagline {
    position: absolute; right: 62px; top: 780px;
    text-align: right; color: var(--white);
    font-family: "Montserrat", sans-serif;
    font-size: 33px; line-height: 42px; letter-spacing: 1.5px;
    text-transform: uppercase;
  }
  .tagline__bold { display: block; font-weight: 700; }
  .tagline__light { display: block; font-weight: 300; }
</style>
</head>
<body>
<main class="sheet">

  <!-- Back: description and contact details -->
  <section class="flyer flyer--back">
    <svg class="flyer__shapes" viewBox="0 0 474 1001" preserveAspectRatio="none">
      <defs>
        <linearGradient id="bathroomTone" x1="0" y1="0" x2="1" y2="1">
          <stop offset="0" stop-color="#b9bcbc"/>
          <stop offset="0.6" stop-color="#e4e4e1"/>
          <stop offset="1" stop-color="#f6f5f1"/>
        </linearGradient>
        <linearGradient id="diningTone" x1="0" y1="0" x2="1" y2="1">
          <stop offset="0" stop-color="#7a4a2e"/>
          <stop offset="1" stop-color="#c98a55"/>
        </linearGradient>
        <linearGradient id="bedroomTone" x1="0" y1="0" x2="1" y2="1">
          <stop offset="0" stop-color="#d9c9a3"/>
          <stop offset="0.5" stop-color="#c9b65a"/>
          <stop offset="1" stop-color="#8c8fa0"/>
        </linearGradient>
      </defs>
      <polygon points="0,0 432,0 384,150 0,150" fill="var(--teal)"/>
      <polygon points="444,0 474,0 474,200 380,200 396,150" fill="var(--grey-strip)"/>
      <polygon points="0,186 300,186 282,402 0,402" fill="url(#bathroomTone)" role="img" aria-label="Photo of a modern bathroom basin with white flowers"/>
      <polygon points="316,186 474,186 474,292 300,292" fill="url(#diningTone)" role="img" aria-label="Photo of a dining table with flowers in a vase"/>
      <polygon points="298,302 474,302 474,432 288,432" fill="url(#bedroomTone)" role="img" aria-label="Photo of a made bed with yellow cushions and a patterned throw"/>
      <polygon points="0,676 474,662 474,1001 0,1001" fill="var(--teal)"/>
    </svg>

    <h2 class="headline">
      <span class="headline__light">What we do</span>
      <span class="headline__bold">Differently!</span>
    </h2>

    <div class="intro">
      <p><span class="intro__dropcap">R</span>ather than relying upon a key safe or a central pick-up destination, a ‘Harbourline Stays’ staff member will greet guests upon arrival.</p>
      <p>Our ‘Meet &amp; Greet’ service provides home owners with an increased level of Security and also allows us to:</p>
      <p>Prepare the home for their arrival (lights, heaters, music etc.) Establish a rapport &amp; help facilitate future bookings. Reiterate their responsibilities to ensure the return of their bond.</p>
    </div>

    <div class="contact">
      <p class="contact__lead">If you’d like to know what your property<br>could achieve or require additional information,<br>please contact us on:</p>
      <ul class="contact__list">
        <li>
          <svg class="contact__icon" viewBox="0 0 18 18" fill="none" stroke="#fff" stroke-width="1.5" stroke-linecap="round" stroke-linejoin="round">
            <path d="M4 2.5l3 3-1.8 1.8a9 9 0 0 0 5.5 5.5L12.5 11l3 3-2 2C7.5 16 2 10.5 2 4.5z"/>
          </svg>
          (03)5900 1234
        </li>
        <li>
          <svg class="contact__icon" viewBox="0 0 18 18" fill="none" stroke="#fff" stroke-width="1.5" stroke-linejoin="round">
            <rect x="2" y="4" width="14" height="10"/>
            <path d="M2 4l7 6 7-6"/>
          </svg>
          stay@harbourlinestays.com.au
        </li>
        <li>
          <svg class="contact__icon" viewBox="0 0 18 18" fill="none" stroke="#fff" stroke-width="1.5" stroke-linecap="round">
            <path d="M7.5 10.5l3-3"/>
            <path d="M8 5l1.5-1.5a3 3 0 0 1 4.2 4.2L12.2 9.2"/>
            <path d="M10 13l-1.5 1.5a3 3 0 0 1-4.2-4.2L5.8 8.8"/>
          </svg>
          harbourlinestays.com.au
        </li>
      </ul>
      <p class="contact__address">PO Box 12, Seaview Victoria 3900</p>
    </div>
  </section>

  <!-- Front: brand, main image and grab line -->
  <section class="flyer flyer--front">
    <svg class="flyer__shapes" viewBox="0 0 469 1001" preserveAspectRatio="none">
      <defs>
        <linearGradient id="swimTone" x1="0" y1="0" x2="1" y2="1">
          <stop offset="0" stop-color="#2fa6b5"/>
          <stop offset="1" stop-color="#5fd0d0"/>
        </linearGradient>
        <linearGradient id="bayTone" x1="0" y1="0" x2="0" y2="1">
          <stop offset="0" stop-color="#9cc6e0"/>
          <stop offset="0.55" stop-color="#7fb2c9"/>
          <stop offset="1" stop-color="#2f7fa0"/>
        </linearGradient>
        <linearGradient id="houseTone" x1="0" y1="0" x2="0" y2="1">
          <stop offset="0" stop-color="#2a2a4a"/>
          <stop offset="0.55" stop-color="#4a3f55"/>
          <stop offset="0.75" stop-color="#2d7fc4"/>
          <stop offset="1" stop-color="#3fb2e6"/>
        </linearGradient>
      </defs>
      <polygon points="0,0 170,0 84,250 0,312" fill="url(#swimTone)" role="img" aria-label="Photo of swimmers in clear turquoise water"/>
      <polygon points="184,0 469,0 469,270 96,270" fill="var(--teal)"/>
      <polygon points="0,330 72,296 72,660 0,660" fill="url(#bayTone)" role="img" aria-label="Photo of a sailing boat moored on a calm bay"/>
      <polygon points="92,286 469,286 469,660 84,660" fill="url(#houseTone)" role="img" aria-label="Photo of a modern house at dusk with a lit swimming pool"/>
      <polygon points="0,690 72,672 469,655 469,1001 0,1001" fill="var(--teal)"/>
    </svg>

    <div class="brand">
      HARBOURLINE<br>STAYS
      <span class="brand__mark"></span>
    </div>

    <h1 class="tagline">
      <span class="tagline__bold">Holiday</span>
      <span class="tagline__light">Rental</span>
      <span class="tagline__light">Management</span>
      <span class="tagline__light">with a</span>
      <span class="tagline__bold">Difference</span>
    </h1>
  </section>

</main>
</body>
</html>
```